New Zealand Export company needs business cards

We need new business cards to match our new logo for a company based in New Zealand who deal specifically with the Pacific Islands. We source, consolidate and ship products out of New Zealand to the Pacific Islands. Will attach our old ones and also new logo.
Would like the Islands we deal with and the areas of work we have access to, to be included on the business cards.

Contact Information for Business Card

T +64 9 571 3048
F +64 9 571 6285
12-18 Kowhai Lane, Drury, 2113
PO Box 814, Drury, Auckland 2247, New Zealand
www.falconfreight.example.nz
E sales@falconfreight.example.nz

Font styles to use
Sans Serif

Colors
85abd2
33a6d7
ffffff

Requirements
Must have
• A company of PWM

```html
<!DOCTYPE html>
<html lang="en">
<head>
<meta charset="utf-8">
<title>Falcon Freight – Business Card</title>
<link href="https://fonts.googleapis.com/css2?family=Arimo:wght@400;700&display=swap" rel="stylesheet">
<style>
  :root {
    --page-bg: #2a2a2a;
    --brand-blue: #0d55a3;
    --accent-blue: #33a6d7;
    --soft-blue: #85abd2;
    --white: #ffffff;
    --card-white: #f2f2f2;
    --ink: #222222;
    --rule: #b8b8b8;
  }
  * { box-sizing: border-box; margin: 0; padding: 0; }
  html, body { width: 1200px; height: 900px; overflow: hidden; }
  body {
    background: var(--page-bg);
    font-family: "Arimo", Arial, sans-serif;
    display: flex;
    flex-direction: column;
    align-items: center;
    justify-content: center;
    gap: 40px;
  }
  .card {
    width: 660px;
    height: 377px;
    position: relative;
    box-shadow: 0 10px 30px rgba(0,0,0,.45);
  }

  /* Front */
  .card-front { background: var(--brand-blue); color: var(--white); }
  .brand {
    position: absolute;
    top: 78px; left: 0; right: 0;
    display: flex; align-items: center; justify-content: center; gap: 16px;
  }
  .brand-square { width: 38px; height: 38px; background: var(--white); }
  .brand-name {
    font-weight: 700; font-size: 40px; letter-spacing: 2px; color: var(--white);
  }
  .service-list { position: absolute; left: 36px; right: 36px; top: 200px; }
  .service-row { display: flex; gap: 14px; margin-bottom: 22px; }
  .service-label {
    flex: 0 0 120px; font-weight: 700; font-size: 15px; white-space: nowrap;
  }
  .service-label::before {
    content: ""; display: inline-block; margin-right: 7px;
    border-left: 9px solid var(--white);
    border-top: 6px solid transparent; border-bottom: 6px solid transparent;
  }
  .service-items { font-size: 11.5px; line-height: 1.45; padding-top: 2px; }

  /* Back */
  .card-back { background: var(--card-white); color: var(--ink); }
  .person { position: absolute; left: 150px; top: 130px; text-align: right; }
  .person-name {
    font-weight: 700; font-size: 25px; color: var(--accent-blue); letter-spacing: .5px;
  }
  .person-title { font-size: 17px; margin-top: 2px; }
  .divider {
    position: absolute; left: 352px; top: 64px; width: 1px; height: 150px;
    background: var(--rule);
  }
  .contact-list { position: absolute; left: 376px; top: 70px; list-style: none; }
  .contact-item {
    display: flex; align-items: center; gap: 12px;
    font-size: 13.5px; height: 34px;
  }
  .contact-icon { width: 20px; height: 20px; flex: 0 0 20px; }
  .address {
    position: absolute; left: 50px; bottom: 50px; font-size: 14px; line-height: 1.5;
  }
  .partner {
    position: absolute; right: 44px; bottom: 86px;
    display: flex; align-items: center; gap: 8px;
  }
  .partner-mark { width: 14px; height: 14px; border-radius: 50%; background: var(--brand-blue); }
  .partner-name {
    font-weight: 700; font-size: 20px; color: var(--brand-blue); letter-spacing: 1px;
  }
</style>
</head>
<body>

  <section class="card card-front">
    <div class="brand">
      <span class="brand-square"></span>
      <span class="brand-name">FALCON FREIGHT</span>
    </div>
    <div class="service-list">
      <div class="service-row">
        <span class="service-label">Islands:</span>
        <p class="service-items">Cook Islands-Papua New Guinea-Tahiti-Tuvalu-Tokelau-Fiji-Kiribati-Samoa-New Caledonia-Tonga-Norfolk Island-Solomon Islands-Vanuatu</p>
      </div>
      <div class="service-row">
        <span class="service-label">Industries:</span>
        <p class="service-items">Hardware-Automobile-Homewares-Aid solutions-Hospitality-Safety Equipment-Environmental Resources</p>
      </div>
    </div>
  </section>

  <section class="card card-back">
    <div class="person">
      <h1 class="person-name">TESSA ROWLEY</h1>
      <p class="person-title">Sales Manager</p>
    </div>
    <span class="divider"></span>
    <ul class="contact-list">
      <li class="contact-item">
        <svg class="contact-icon" viewBox="0 0 24 24" fill="none" stroke="var(--accent-blue)" stroke-width="1.6"><path d="M5 3h4l2 5-3 2a11 11 0 0 0 6 6l2-3 5 2v4a2 2 0 0 1-2 2A17 17 0 0 1 3 5a2 2 0 0 1 2-2z"/></svg>
        <span>+64 9 571 3048</span>
      </li>
      <li class="contact-item">
        <svg class="contact-icon" viewBox="0 0 24 24" fill="var(--accent-blue)"><path d="M2 8c3-4 17-4 20 0l-1 3h-4l-1-2H8l-1 2H3z"/><rect x="5" y="12" width="14" height="9" rx="1.5"/><circle cx="12" cy="16.5" r="2.2" fill="var(--card-white)"/></svg>
        <span>+64 9 571 6285</span>
      </li>
      <li class="contact-item">
        <svg class="contact-icon" viewBox="0 0 24 24" fill="var(--accent-blue)"><rect x="2" y="5" width="20" height="14" rx="1"/><path d="M2 6l10 7 10-7" fill="none" stroke="var(--card-white)" stroke-width="1.5"/></svg>
        <span>E sales@falconfreight.example.nz</span>
      </li>
      <li class="contact-item">
        <svg class="contact-icon" viewBox="0 0 24 24" fill="none" stroke="var(--accent-blue)" stroke-width="1.4"><circle cx="12" cy="12" r="9.5"/><ellipse cx="12" cy="12" rx="4.5" ry="9.5"/><path d="M2.5 12h19M4 7h16M4 17h16"/></svg>
        <span>www.falconfreight.example.nz</span>
      </li>
    </ul>
    <address class="address" style="font-style:normal">
      12-18 Kowhai Lane, Drury, 2113<br>
      PO Box 814, Drury, Auckland 2247, New Zealand
    </address>
    <div class="partner">
      <span class="partner-mark"></span>
      <span class="partner-name">PWM</span>
    </div>
  </section>

</body>
</html>
```